Bath Salt - Sachet Packet (5 Scents) Packaging Design

We sell products to professional salons in the USA. This product is used as the first step when treating clients to a pedicure spa. This product is called SALT SOAK (or Bath Salts). The salt is added to the water to cleanse the skin, create a pleasant fragrance, and change the color of the water.

This product has 5 different variations, based on the scent of the salt soak. The available scents are:
LAVENDER, MANDARIN, CUCUMBER-MELON, JASMINE, MINT.

We would like to see package designs for all 5 scents. The theme should be consistent across the different variations of scents. The design should focus on bright, attractive, floral colors/themes. The design should fully express the color and imagery that are associated with each scent. (Lavender scent should include purple colors, lavender flower, etc.). See example images for reference of popular designs/brands.

Ideal designs will incorporate a luxurious and premium aesthetic that combines elegant imagery, colors, and premium finishes. See example images for reference of popular designs/brands.

Each packet is individually sealed. See dimension artwork file for reference of the sachet packet size and layout.

See the attached document guidelines for more information about product name, key text, and brand logo.

Target Market(s)

Beauty & Nail Salons

Industry/Entity Type

Beauty

Font styles to use
Sans Serif
Script

Requirements
Must have
• Bright imagery and colors that relate to the target fragrance
Nice to have
• Premium and luxurious finishes (shiny accent, etc.)

```html
<!DOCTYPE html>
<html lang="en">
<head>
<meta charset="utf-8">
<title>Sea Salt Soak Sachets</title>
<link href="https://fonts.googleapis.com/css2?family=Lexend:wght@300;400;500&family=Mrs+Saint+Delafield&family=Libre+Franklin:wght@400;500&display=swap" rel="stylesheet">
<style>
  :root{
    --page:#ececec;
    --card:#ffffff;
    --ink:#1c1c1c;
    --lavender:#7a5ce0; --lavender-arch:#f7f2fb; --lavender-art-a:#8b78e6; --lavender-art-b:#b9c7a6;
    --mandarin:#f0622a; --mandarin-arch:#fdf1ec; --mandarin-art-a:#f2753a; --mandarin-art-b:#3f7a3a;
    --cucumber:#c6d92c; --cucumber-arch:#f4fae6; --cucumber-art-a:#7fbf4d; --cucumber-art-b:#f0a070;
    --jasmine:#2f7a2c; --jasmine-arch:#fbfbea; --jasmine-art-a:#2f6f3a; --jasmine-art-b:#eef3e8;
    --mint:#3fd45c; --mint-arch:#edfbf1; --mint-art-a:#2f8a3a; --mint-art-b:#7ccf5e;
  }
  *{box-sizing:border-box;margin:0;padding:0}
  html,body{width:1200px;height:768px;overflow:hidden;background:var(--page)}
  .sheet{position:relative;width:1200px;height:768px}
  .row{position:absolute;left:26px;display:flex;gap:18.5px}
  .row.fronts{top:22px}
  .row.backs{top:398px}
  .card{position:relative;width:215px;height:349px;background:var(--card);overflow:hidden}
  .lavender{--accent:var(--lavender);--arch:var(--lavender-arch);--art-a:var(--lavender-art-a);--art-b:var(--lavender-art-b)}
  .mandarin{--accent:var(--mandarin);--arch:var(--mandarin-arch);--art-a:var(--mandarin-art-a);--art-b:var(--mandarin-art-b)}
  .cucumber{--accent:var(--cucumber);--arch:var(--cucumber-arch);--art-a:var(--cucumber-art-a);--art-b:var(--cucumber-art-b)}
  .jasmine{--accent:var(--jasmine);--arch:var(--jasmine-arch);--art-a:var(--jasmine-art-a);--art-b:var(--jasmine-art-b)}
  .mint{--accent:var(--mint);--arch:var(--mint-arch);--art-a:var(--mint-art-a);--art-b:var(--mint-art-b)}

  .botanical-frame{position:absolute;left:10px;top:26px;width:196px;height:300px;border-radius:40px;
    background:radial-gradient(ellipse at 30% 25%,var(--art-a) 0%,transparent 60%),
               radial-gradient(ellipse at 75% 80%,var(--art-b) 0%,transparent 60%),
               radial-gradient(ellipse at 50% 50%,var(--art-a) 0%,transparent 75%);opacity:.55}
  .arch{position:absolute;left:41px;top:74px;width:133px;height:202px;background:var(--arch);border-radius:66.5px 66.5px 0 0}
  .brand{font-family:"Lexend",sans-serif;font-weight:400;color:var(--ink);font-size:17px;letter-spacing:.2px;text-align:center;display:flex;align-items:center;justify-content:center;gap:3px}
  .brand .dot{width:3px;height:3px;border-radius:50%;background:var(--ink);display:inline-block}
  .arch .brand{position:absolute;top:24px;width:100%}
  .scent{position:absolute;width:100%;text-align:center;font-family:"Mrs Saint Delafield",cursive;color:var(--accent);font-size:34px;line-height:28px;top:80px}
  .scent.two-line{top:52px;line-height:27px;font-size:32px}
  .product{position:absolute;top:111px;left:-20px;right:-20px;text-align:center;font-family:"Lexend",sans-serif;font-weight:300;font-size:13.5px;letter-spacing:.6px;color:var(--ink)}
  .claim{position:absolute;top:166px;width:100%;text-align:center;font-family:"Lexend",sans-serif;font-size:5.8px;letter-spacing:.6px;color:var(--accent)}

  .botanical-band{position:absolute;left:0;top:0;width:100%;height:52px;
    background:radial-gradient(ellipse at 20% 40%,var(--art-a) 0%,transparent 55%),
               radial-gradient(ellipse at 60% 50%,var(--art-b) 0%,transparent 55%),
               radial-gradient(ellipse at 90% 30%,var(--art-a) 0%,transparent 50%);opacity:.6}
  .back .brand{position:absolute;top:60px;width:100%}
  .info{position:absolute;left:0;width:100%;text-align:center;font-family:"Libre Franklin",sans-serif;color:var(--ink);font-size:7.4px;line-height:9.1px}
  .info h3{font-weight:400;font-size:7.4px;color:var(--accent)}
  .directions{top:92px}
  .ingredients{top:128px}
  .caution{top:182px}
  .distributor{top:271px;font-size:5.4px;line-height:6.8px}
  .origin{top:317px;font-weight:500}
  .mint .distributor.large{top:276px;font-size:7.4px;line-height:9.1px}
  .mint .origin.large{top:327px}
</style>
</head>
<body>
<main class="sheet">
  <section class="row fronts">
    <article class="card front lavender">
      <div class="botanical-frame" role="img" aria-label="Watercolor lavender sprigs framing the label"></div>
      <div class="arch">
        <div class="brand"><span>Solea</span><span class="dot"></span></div>
        <div class="scent">Lavender</div>
        <div class="product">Sea Salt Soak</div>
        <div class="claim">Paraben Free</div>
      </div>
    </article>
    <article class="card front mandarin">
      <div class="botanical-frame" role="img" aria-label="Watercolor mandarin oranges, blossoms and leaves framing the label"></div>
      <div class="arch">
        <div class="brand"><span>Solea</span><span class="dot"></span></div>
        <div class="scent">Mandarin</div>
        <div class="product">Sea Salt Soak</div>
        <div class="claim">Paraben Free</div>
      </div>
    </article>
    <article class="card front cucumber">
      <div class="botanical-frame" role="img" aria-label="Watercolor cucumbers, cucumber slices, melon wedges and leaves framing the label"></div>
      <div class="arch">
        <div class="brand"><span>Solea</span><span class="dot"></span></div>
        <div class="scent two-line">Cucumber<br>Melon</div>
        <div class="product">Sea Salt Soak</div>
        <div class="claim">Paraben Free</div>
      </div>
    </article>
    <article class="card front jasmine">
      <div class="botanical-frame" role="img" aria-label="Watercolor jasmine blossoms and dark green leaves framing the label"></div>
      <div class="arch">
        <div class="brand"><span>Solea</span><span class="dot"></span></div>
        <div class="scent">Jasmine</div>
        <div class="product">Sea Salt Soak</div>
        <div class="claim">Paraben Free</div>
      </div>
    </article>
    <article class="card front mint">
      <div class="botanical-frame" role="img" aria-label="Watercolor mint leaves framing the label"></div>
      <div class="arch">
        <div class="brand"><span>Solea</span><span class="dot"></span></div>
        <div class="scent">Mint</div>
        <div class="product">Sea Salt Soak</div>
        <div class="claim">Paraben Free</div>
      </div>
    </article>
  </section>

  <section class="row backs">
    <article class="card back lavender">
      <div class="botanical-band" role="img" aria-label="Watercolor lavender sprigs along the top edge"></div>
      <div class="brand"><span>Solea</span><span class="dot"></span></div>
      <div class="info directions"><h3>DIRECTIONS:</h3><p>Add desired amount to warm water, soak feet,<br>and then rinse.</p></div>
      <div class="info ingredients"><h3>INGREDIENTS:</h3><p>Lorem ipsum dolor sit amet, consectetur<br>adipiscing elit, sed do eiusmod tempor incididunt<br>ut<br>labore et dolore magna aliqua.</p></div>
      <div class="info caution"><h3>CAUTION:</h3><p>For external use only. Avoid use when skin is<br>damaged or near any open cuts, wounds, or<br>irritations. If signs of irritation occur, stop use<br>immediately and consult a doctor. Keep away<br>from direct sunlight. Store at room temperature<br>and use immediately after opening. Keep out<br>of reach of children.</p></div>
      <div class="info distributor"><p>Distributed by:<br>Blue Harbor Supply, Inc.<br>Fairview, IN 46012<br>www.blueharborsupply.com</p></div>
      <div class="info origin">Made in Korea</div>
    </article>
    <article class="card back mandarin">
      <div class="botanical-band" role="img" aria-label="Watercolor mandarin oranges and leaves along the top edge"></div>
      <div class="brand"><span>Solea</span><span class="dot"></span></div>
      <div class="info directions"><h3>DIRECTIONS:</h3><p>Add desired amount to warm water, soak feet,<br>and then rinse.</p></div>
      <div class="info ingredients"><h3>INGREDIENTS:</h3><p>Lorem ipsum dolor sit amet, consectetur<br>adipiscing elit, sed do eiusmod tempor incididunt<br>ut<br>labore et dolore magna aliqua.</p></div>
      <div class="info caution"><h3>CAUTION:</h3><p>For external use only. Avoid use when skin is<br>damaged or near any open cuts, wounds, or<br>irritations. If signs of irritation occur, stop use<br>immediately and consult a doctor. Keep away<br>from direct sunlight. Store at room temperature<br>and use immediately after opening. Keep out<br>of reach of children.</p></div>
      <div class="info distributor"><p>Distributed by:<br>Blue Harbor Supply, Inc.<br>Fairview, IN 46012<br>www.blueharborsupply.com</p></div>
      <div class="info origin">Made in Korea</div>
    </article>
    <article class="card back cucumber">
      <div class="botanical-band" role="img" aria-label="Watercolor cucumber slices, melon and leaves along the top edge"></div>
      <div class="brand"><span>Solea</span><span class="dot"></span></div>
      <div class="info directions"><h3>DIRECTIONS:</h3><p>Add desired amount to warm water, soak feet,<br>and then rinse.</p></div>
      <div class="info ingredients"><h3>INGREDIENTS:</h3><p>Lorem ipsum dolor sit amet, consectetur<br>adipiscing elit, sed do eiusmod tempor incididunt<br>ut<br>labore et dolore magna aliqua.</p></div>
      <div class="info caution"><h3>CAUTION:</h3><p>For external use only. Avoid use when skin is<br>damaged or near any open cuts, wounds, or<br>irritations. If signs of irritation occur, stop use<br>immediately and consult a doctor. Keep away<br>from direct sunlight. Store at room temperature<br>and use immediately after opening. Keep out<br>of reach of children.</p></div>
      <div class="info distributor"><p>Distributed by:<br>Blue Harbor Supply, Inc.<br>Fairview, IN 46012<br>www.blueharborsupply.com</p></div>
      <div class="info origin">Made in Korea</div>
    </article>
    <article class="card back jasmine">
      <div class="botanical-band" role="img" aria-label="Watercolor jasmine blossoms and leaves along the top edge"></div>
      <div class="brand"><span>Solea</span><span class="dot"></span></div>
      <div class="info directions"><h3>DIRECTIONS:</h3><p>Add desired amount to warm water, soak feet,<br>and then rinse.</p></div>
      <div class="info ingredients"><h3>INGREDIENTS:</h3><p>Lorem ipsum dolor sit amet, consectetur<br>adipiscing elit, sed do eiusmod tempor incididunt<br>ut<br>labore et dolore magna aliqua.</p></div>
      <div class="info caution"><h3>CAUTION:</h3><p>For external use only. Avoid use when skin is<br>damaged or near any open cuts, wounds, or<br>irritations. If signs of irritation occur, stop use<br>immediately and consult a doctor. Keep away<br>from direct sunlight. Store at room temperature<br>and use immediately after opening. Keep out<br>of reach of children.</p></div>
      <div class="info distributor"><p>Distributed by:<br>Blue Harbor Supply, Inc.<br>Fairview, IN 46012<br>www.blueharborsupply.com</p></div>
      <div class="info origin">Made in Korea</div>
    </article>
    <article class="card back mint">
      <div class="botanical-band" role="img" aria-label="Watercolor mint leaves along the top edge"></div>
      <div class="brand"><span>Solea</span><span class="dot"></span></div>
      <div class="info directions"><h3>DIRECTIONS:</h3><p>Add desired amount to warm water, soak feet,<br>and then rinse.</p></div>
      <div class="info ingredients"><h3>INGREDIENTS:</h3><p>Lorem ipsum dolor sit amet, consectetur<br>adipiscing elit, sed do eiusmod tempor incididunt<br>ut<br>labore et dolore magna aliqua.</p></div>
      <div class="info caution"><h3>CAUTION:</h3><p>For external use only. Avoid use when skin is<br>damaged or near any open cuts, wounds, or<br>irritations. If signs of irritation occur, stop use<br>immediately and consult a doctor. Keep away<br>from direct sunlight. Store at room temperature<br>and use immediately after opening. Keep out<br>of reach of children.</p></div>
      <div class="info distributor large"><p>Distributed by:<br>Blue Harbor Supply, Inc.<br>Fairview, IN 46012<br>www.blueharborsupply.com</p></div>
      <div class="info origin large">Made in Korea</div>
    </article>
  </section>
</main>
</body>
</html>
```